Design einer Angebotsmappe
Super Zusammenarbeit! Wir sind sehr zufrieden. LG
Zielgruppe
Wir sind ein Handwerksbetrieb im Bereich Elektrotechnik.
Wir betreuen private Haushalte, Gewerbekunden oder Architekten.
Mehr über uns : www.falkner-rieben.de
Aufgabenstellung
Es soll das Design für eine Angebotsmappe erstellt werden. Die Mappe soll einen sehr hochwertigen und professionellen Eindruck beim Kunden machen.
Unser Logo soll auf der Vorderseite platziert werden und mit partiellen UV Lack in Szene gesetzt werden.
Alles andere ist Ihrer Kreativität überlassen.
-An geeigneter Stelle soll auf unsere Profile bei Pixmora & Freundeshub hingewiesen werden mit passenden Icon und Accountname.
-Sowie ein Hinweis auf unsere Internetseite www.falkner-rieben.de
Zu beachten sind die Druckvorgaben im Anhang

```html
<!DOCTYPE html>
<html lang="de">
<head>
<meta charset="utf-8">
<title>Angebotsmappe – Falkner &amp; Rieben Elektrotechnik</title>
<link href="https://fonts.googleapis.com/css2?family=Montserrat:wght@500;700&family=Roboto:wght@400;500;700&display=swap" rel="stylesheet">
<style>
:root{
  --stage:#e4e5e7;
  --paper:#fbfbfb;
  --paper-shade:#f1f2f3;
  --blue:#2a97c9;
  --blue-deep:#1f7fb0;
  --blue-soft:#d9ecf5;
  --ink:#2e3236;
  --ink-soft:#6b7075;
  --rule:#d4d7da;
}
*{box-sizing:border-box;margin:0;padding:0}
html,body{width:1200px;height:900px;overflow:hidden}
body{background:var(--stage);font-family:"Roboto",Arial,sans-serif;color:var(--ink);position:relative}
.spread{position:absolute;display:flex;box-shadow:0 6px 18px rgba(0,0,0,.12)}
.spread--outside{left:330px;top:40px}
.spread--inside{left:195px;top:462px}
.panel{width:270px;height:382px;background:var(--paper);position:relative;overflow:hidden}
.panel + .panel{border-left:1px solid var(--rule)}

/* brand name lockup */
.brand{display:flex;flex-direction:column;align-items:center;gap:4px;font-family:"Montserrat",Arial,sans-serif;font-weight:700;color:var(--blue);text-align:center}
.brand__dot{width:16px;height:16px;border-radius:50%;background:var(--blue)}
.brand__name{font-size:19px;letter-spacing:.5px;line-height:1}
.brand__sub{font-size:8px;letter-spacing:3px;line-height:1}

/* outside: service flap */
.services{padding:34px 26px 0}
.service{display:flex;gap:12px;align-items:flex-start;margin-bottom:20px}
.service__icon{width:28px;height:28px;border-radius:50%;border:1.5px solid var(--blue);flex:none;display:flex;align-items:center;justify-content:center}
.service__icon svg{width:14px;height:14px;fill:var(--blue)}
.service__title{font-size:8.5px;font-weight:700;color:var(--blue);margin-bottom:3px}
.service__text{font-size:7px;color:var(--ink-soft);line-height:1.4}
.web{position:absolute;left:26px;bottom:52px;font-family:"Montserrat",Arial,sans-serif;font-weight:700;font-size:13px;color:var(--blue)}
.contact{position:absolute;left:26px;right:26px;bottom:18px;display:flex;justify-content:space-between;font-size:6px;color:var(--ink-soft);border-top:1px solid var(--rule);padding-top:6px}

/* outside: cover */
.cover{display:flex;align-items:center;justify-content:center}

/* inside: welcome */
.welcome{display:flex;flex-direction:column;justify-content:center;align-items:center;text-align:center;background:linear-gradient(160deg,var(--paper),var(--paper-shade))}
.welcome__line{font-family:"Montserrat",Arial,sans-serif;font-weight:700;color:var(--blue);font-size:11px;line-height:1.35}
.welcome__small{font-family:"Montserrat",Arial,sans-serif;font-weight:500;color:var(--blue);font-size:8px;margin-top:3px}

/* inside: letter + pocket */
.middle{background:var(--paper-shade)}
.letter{position:absolute;left:18px;top:12px;width:234px;height:330px;background:#fff;box-shadow:0 1px 4px rgba(0,0,0,.1);padding:18px 18px;font-size:5.4px;line-height:1.45}
.letter .brand{position:absolute;right:16px;top:14px;gap:2px}
.letter .brand__dot{width:7px;height:7px}
.letter .brand__name{font-size:8px}
.letter .brand__sub{font-size:4px;letter-spacing:1.5px}
.letter__recipient{margin-top:38px;font-weight:700}
.letter__meta{text-align:right;margin-top:8px;color:var(--ink-soft)}
.letter__subject{font-weight:700;font-size:6.5px;margin:12px 0 8px}
.letter p{margin-bottom:6px;color:var(--ink)}
.letter__names{margin-top:18px;color:var(--ink-soft)}
.pocket{position:absolute;left:10px;right:10px;bottom:0;height:94px;background:var(--paper);border-radius:26px 26px 0 0;box-shadow:0 -2px 6px rgba(0,0,0,.08);padding:14px 14px}
.card{position:absolute;left:14px;top:12px;width:104px;height:62px;background:var(--blue);display:flex;align-items:center;justify-content:center}
.card .brand{color:#fff;gap:2px}
.card .brand__dot{width:7px;height:7px;background:#fff}
.card .brand__name{font-size:8.5px}
.card .brand__sub{font-size:4px;letter-spacing:1.5px}
.socials{position:absolute;left:128px;top:22px;font-size:5.6px;font-weight:700;color:var(--ink)}
.social{display:flex;align-items:center;gap:4px;margin-bottom:6px}
.social__mark{width:8px;height:8px;border-radius:50%;background:var(--ink);flex:none}
.social__label{display:block;font-weight:400;color:var(--ink-soft);font-size:5px}

/* inside: photo insert */
.insert{position:absolute;left:18px;top:14px;width:234px;height:354px;background:var(--blue);padding:0 0 16px;color:#fff;font-size:5.6px;line-height:1.45}
.insert__photo{height:250px;background:linear-gradient(180deg,#6cc0e4 0%,#3aa3d2 55%,#2a8fc0 100%)}
.insert__text{padding:10px 12px 0}
.insert__text p{margin-bottom:5px}
</style>
</head>
<body>

<section class="spread spread--outside" aria-label="Außenseite der Mappe">
  <div class="panel">
    <div class="services">
      <div class="service">
        <div class="service__icon"><svg viewBox="0 0 14 14"><path d="M8 0 2 8h4l-1 6 6-8H7z"/></svg></div>
        <div><div class="service__title">Elektroinstallation</div><div class="service__text">Neubau, Altbau und Sanierung aus einer Hand</div></div>
      </div>
      <div class="service">
        <div class="service__icon"><svg viewBox="0 0 14 14"><circle cx="7" cy="7" r="3.2"/><rect x="6" y="0" width="2" height="3"/><rect x="6" y="11" width="2" height="3"/><rect x="0" y="6" width="3" height="2"/><rect x="11" y="6" width="3" height="2"/></svg></div>
        <div><div class="service__title">Gebäudetechnik</div><div class="service__text">Smarte Steuerung für Licht und Heizung</div></div>
      </div>
      <div class="service">
        <div class="service__icon"><svg viewBox="0 0 14 14"><rect x="1" y="1" width="12" height="3"/><rect x="1" y="5.5" width="12" height="3"/><rect x="1" y="10" width="12" height="3"/></svg></div>
        <div><div class="service__title">Zählerschränke</div><div class="service__text">Planung, Aufbau und Prüfung nach Norm</div></div>
      </div>
      <div class="service">
        <div class="service__icon"><svg viewBox="0 0 14 14"><rect x="4" y="0" width="1.6" height="4"/><rect x="8.4" y="0" width="1.6" height="4"/><path d="M2 4h10v3a5 5 0 0 1-4 4.9V14H6v-2.1A5 5 0 0 1 2 7z"/></svg></div>
        <div><div class="service__title">E-Mobilität</div><div class="service__text">Wallboxen für Garage und Firmenhof</div></div>
      </div>
      <div class="service">
        <div class="service__icon"><svg viewBox="0 0 14 14"><path d="M3 1h3l1 3-2 1.5a8 8 0 0 0 3.5 3.5L10 7l3 1v3a2 2 0 0 1-2 2A10 10 0 0 1 1 3a2 2 0 0 1 2-2z"/></svg></div>
        <div><div class="service__title">Kundendienst</div><div class="service__text">Schnelle Hilfe bei Störungen vor Ort</div></div>
      </div>
    </div>
    <div class="web">www.falkner-rieben.de</div>
    <div class="contact"><span>Lindenweg 14, 21465 Haselbrook</span><span>040 555 218 40</span><span>info@falkner-rieben.de</span></div>
  </div>
  <div class="panel cover">
    <div class="brand">
      <span class="brand__dot"></span>
      <span class="brand__name">FALKNER &amp; RIEBEN</span>
      <span class="brand__sub">ELEKTROTECHNIK</span>
    </div>
  </div>
</section>

<section class="spread spread--inside" aria-label="Innenseite der Mappe">
  <div class="panel welcome">
    <div class="welcome__line">Willkommen<br>bei Ihrem Elektriker in Haselbrook</div>
    <div class="welcome__small">Falkner &amp; Rieben Elektrotechnik</div>
  </div>

  <div class="panel middle">
    <article class="letter">
      <div class="brand">
        <span class="brand__dot"></span>
        <span class="brand__name">FALKNER &amp; RIEBEN</span>
        <span class="brand__sub">ELEKTROTECHNIK</span>
      </div>
      <div class="letter__recipient">Musterfirma<br>Musterabteilung<br>Muster Str. 57<br>76543 Musterdorf</div>
      <div class="letter__meta">Lindenweg 14, 21465 Haselbrook, 20. April 2020</div>
      <div class="letter__subject">Moin moin</div>
      <p>Sehr geehrter Herr Muster,</p>
      <p>Lorem ipsum dolor sit amet, consectetuer adipiscing elit, sed diam nonummy nibh euismod tincidunt ut laoreet dolore magna aliquam erat volutpat. Ut wisi enim ad minim veniam, quis nostrud exerci tation ullamcorper suscipit lobortis nisl ut aliquip ex ea commodo consequat. Duis autem vel eum iriure dolor in hendrerit in vulputate velit esse molestie consequat.</p>
      <p>Mit freundlichen Grüßen</p>
      <div class="letter__names">Jonas Falkner und Lukas Rieben</div>
    </article>
    <div class="pocket">
      <div class="card">
        <div class="brand">
          <span class="brand__dot"></span>
          <span class="brand__name">FALKNER &amp; RIEBEN</span>
          <span class="brand__sub">ELEKTROTECHNIK</span>
        </div>
      </div>
      <div class="socials">
        <div class="social"><span class="social__mark"></span><span>falkner_rieben_elektrotechnik<span class="social__label">Pixmora</span></span></div>
        <div class="social"><span class="social__mark"></span><span>falknerriebenelektrotechnik<span class="social__label">Freundeshub</span></span></div>
      </div>
    </div>
  </div>

  <div class="panel middle">
    <div class="insert">
      <div class="insert__photo" role="img" aria-label="Foto der beiden Inhaber vor ihren Firmenfahrzeugen, blau eingefärbt"></div>
      <div class="insert__text">
        <p>Die Firma Falkner &amp; Rieben Elektrotechnik GmbH &amp; Co. KG ist Ihr zuverlässiger Partner für alle Fragen in der Elektrotechnik.</p>
        <p>Unser junges, aufstrebendes Unternehmen wurde von Jonas Falkner und Lukas Rieben in Haselbrook gegründet. Wir stehen für einen freundlichen Umgang mit unseren Kunden und für eine fachlich kompetente Beratung vor, während und nach der Bauphase.</p>
        <p>Ihr Elektriker in Haselbrook und Umland!</p>
      </div>
    </div>
  </div>
</section>

</body>
</html>
```